Domestic violence resource cards for distribution to at-risk patients in an emergency department

Using the attached image(or very similar) and text document, a tri-fold business card is requested that integrates the image on the outside and the document content throughout the card's remaining faces. A creative format is requested, one that does not look like the typical cold, uncaring bullet point outlines that are found in similar resource projects. Bold or larger font sizes are requested for headings and body text is not required to be aligned or justified and the bullet points in the supplied document can be removed for creative license. Palattes should be clear, avoiding neons or implied target gender. Legibility is paramount, but again a creative presentation of a very serious subject is our goal. These cards are intended to be distributed to patients or others in the emergency department that may benefit from domestic violence resources. The business card size is mandatory so that the card can be concealed if needed by the receiver.
Updates

Reason: There are several revisions from designers that we are anxiously awaiting; we want to provide time for these designers to submit new designs but also continue spending time with their families and friends around the holiday season.

Target Market(s)

Patients and family in contact with emergency services

Industry/Entity Type

Healthcare

Contact Information for Business Card

Double sided tri-fold card with image on outer sides, text content and resource phone numbers on the exterior. When complete, the card should fold to standard US business card size.

Font styles to use
Other font styles liked:
• Designer's choice, but clear and legible

Requirements
Must have
• See above description. Card must be tri-fold, fold down to standard business card size, remain easily readable, and fold along the long edge.
Should not have
• Cartoon images; bloated fonts or clipart; bright, flashy neon or rainbow-like colors; additional graphics or charts.

```html
<!DOCTYPE html>
<html lang="en">
<head>
<meta charset="utf-8">
<title>Safety Resource Card – Interior</title>
<link href="https://fonts.googleapis.com/css2?family=Montserrat:wght@700&family=Raleway:ital,wght@1,400&display=swap" rel="stylesheet">
<style>
  :root {
    --backdrop: #a6c6de;
    --card: #000000;
    --ink: #f2f2f2;
    --fold: #3a3a3a;
  }
  html, body {
    margin: 0;
    padding: 0;
    width: 900px;
    height: 1200px;
    overflow: hidden;
    background: var(--backdrop);
  }
  .card {
    position: absolute;
    left: 270px;
    top: 330px;
    width: 428px;
    height: 550px;
    background: var(--card);
    color: var(--ink);
    box-sizing: border-box;
  }
  .fold-line {
    position: absolute;
    left: 0;
    width: 100%;
    height: 1px;
    background: var(--fold);
  }
  .fold-line.first { top: 188px; }
  .fold-line.second { top: 368px; }
  .heading {
    font-family: "Montserrat", sans-serif;
    font-weight: 700;
    font-size: 11px;
    line-height: 12px;
    margin: 0;
    letter-spacing: 0.2px;
  }
  .list {
    font-family: "Raleway", sans-serif;
    font-style: italic;
    font-weight: 400;
    text-align: center;
    margin: 0;
    padding: 0;
    list-style: none;
  }
  .signs {
    position: absolute;
    top: 6px;
    left: 6px;
    right: 6px;
  }
  .signs .list {
    font-size: 10.2px;
    line-height: 13.2px;
    margin-top: 2px;
  }
  .remember {
    position: absolute;
    top: 152px;
    left: 16px;
    right: 6px;
  }
  .remember .list,
  .tips .list {
    font-size: 9.4px;
    line-height: 11.5px;
    letter-spacing: 0.6px;
    margin-top: 2px;
  }
  .remember .list { margin-left: -10px; }
  .tips {
    position: absolute;
    top: 256px;
    left: 22px;
    right: 6px;
  }
  .tips .list { margin-left: -16px; margin-top: 3px; }
  .tips .list li { margin-bottom: 0; }
</style>
</head>
<body>
  <section class="card" aria-label="Domestic violence safety card, inside panels">
    <div class="fold-line first"></div>
    <div class="fold-line second"></div>

    <div class="signs">
      <h2 class="heading">Does your partner ever...</h2>
      <ul class="list">
        <li>Hit, kick, push, choke or slap you?</li>
        <li>Intimidate you with weapons or harmful objects?</li>
        <li>Force you to engage in sexual acts?</li>
        <li>Threaten to hurt you, your children or your friends/family?</li>
        <li>Threaten to deport you or tell others your personal information?</li>
        <li>Control where you go, who you talk to or who you make friends with?</li>
        <li>Keep, hide or destroy your most important things?</li>
        <li>Blame, embarrass, or criticize you, make you feel worthless or guilty?</li>
        <li>Control your food, money, medicines or medical care?</li>
        <li>You may be a victim of abuse or neglect!</li>
      </ul>
    </div>

    <div class="remember">
      <h2 class="heading">Always remember...</h2>
      <ul class="list">
        <li>You have a right to be safe anywhere</li>
        <li>You don’t deserve to be hit or threatened</li>
        <li>Your children deserve to grow up without violence</li>
        <li>You have a right to protect you or your children until<br>you are out of danger</li>
        <li>You are not alone</li>
        <li>You have choices</li>
      </ul>
    </div>

    <div class="tips">
      <h2 class="heading">Leaving can be tough and very dangerous. Here are<br>some tips to help you plan for safety:</h2>
      <ul class="list">
        <li>Know people you can talk to and ask them to call the<br>police if they hear a disturbance coming from your home</li>
        <li>Teach your children how to contact the police or fire department</li>
        <li>Practice how to get you and your children out of<br>your home quickly and safely</li>
        <li>Plan where you will go if you have to leave right away<br>and know the location of local emergency shelters</li>
        <li>Leave copies of important papers, keys, cash, IDs,<br>and medicine with a friend or relative you trust</li>
        <li>Have a small bag packed and ready at a friend or<br>relative’s house so you can leave quick</li>
        <li>Stay off social media or cancel you accounts so that you<br>can’t be found online or through your friends</li>
        <li>Do not talk about your plans in public areas or in mixed groups</li>
        <li>Open a credit card or bank account in your name only and<br>do not use it until you are ready</li>
        <li>Keep a charged prepaid cell phone and a shelter<br>hotline number ready for emergencies</li>
        <li>Review your plan often and only share with trusted friends<br>or family</li>
        <li>Be careful: you are at most risk during the first 72 hours<br>after leaving an abusive situation</li>
        <li>Seek help at a police station, firehouse or hospital if needed</li>
      </ul>
    </div>
  </section>
</body>
</html>
```